Store Front Signage for an Upscale Cake & Dessert Bakery

We need a design for store front windows. We are a 12 year old bakery specializing in cakes, cupcakes, cookies, pies, and other desserts. We recently moved to a high traffic location.. and we would like to boost our visual presence; we can be seen from the main road but are competing with other businesses for attention. Attached is a photo of our store front with posters but this signage will be for window film for the entire window span. (see the store front to the left of the photo to see the green and yellow as a film example)
Our logo and store sign (not like in photo, that is showing more red) are in shades of pink. The most visible part of the signage is in the upper third to upper half of the 60" panels.
The signs in the window currently say Life's Short. Eat Cake.
We now use Enjoy Life. Eat Cake.
The design should span all the windows and door -- this can be individual panels or one design that covers all panels. I have pink and greys chosen but please DO NOT let this constrain you. The inside of the bakery has grey floors and walls. white cabinetry, black granite countertops. The only thing with color is the baked goods and display cakes, pictures of cakes, the logo and menu and employee shirts.

Target Market(s)

we are located at a busy intersection --- we would like to capture the attention of people in cars as they pass by and entice them to stop in

Font styles to use
Serif
Sans Serif

Colors
d3d3d3
757575
ffffff
e24197
e667a6
eea4c8
f9d9e8

Requirements
Must have
• I would like the design to be easily discernible at the road way that is about 75 feet from store front. If you look at the photos I provide, note that the font size that is easily readable from the road are the ones in the top panes (although the shadow from the building makes them difficult to see -- the best visibility is the top 1/3 of the 60" panels.
Nice to have
• would like to have some non-photo graphics of a cake ( like a birthday cake), tiered cake, cupcakes, and cookies or pie for the panels --- but DO NOT let this constrain you. I need something to grab attention while cars are stopped at the nearby traffic light.
• If this design works well... I will be changing the panel on a seasonal basis
Should not have
• words that cannot be read from a distance.

```html
<!DOCTYPE html>
<html lang="en">
<head>
<meta charset="utf-8">
<title>Bellamie's Bake Shoppe – Storefront Window Film</title>
<link rel="stylesheet" href="https://fonts.googleapis.com/css2?family=Poppins:ital,wght@1,700;1,800&display=swap">
<style>
  :root {
    --pink-hot: #e24197;
    --pink-mid: #e667a6;
    --pink-soft: #eea4c8;
    --film-black: #0b0b0c;
    --frame-grey: #a6a6a6;
    --frame-edge: #6e6e6e;
    --white: #ffffff;
  }
  html, body {
    margin: 0;
    padding: 0;
    width: 1200px;
    height: 1200px;
    overflow: hidden;
    background: var(--white);
  }
  .storefront { display: block; width: 1200px; height: 1200px; }
  .frame { fill: var(--frame-grey); stroke: var(--frame-edge); stroke-width: 1; }
  .pane-black { fill: var(--film-black); }
  .band-hot { fill: var(--pink-hot); }
  .band-soft { fill: var(--pink-soft); }
  .copy {
    font-family: "Poppins", sans-serif;
    font-style: italic;
    font-weight: 800;
  }
  .copy-white { fill: var(--white); }
  .copy-pink { fill: var(--pink-mid); }
  .headline { font-size: 74px; letter-spacing: -1px; }
  .line-lg { font-size: 46px; }
  .line-md { font-size: 38px; }
  .line-sm { font-size: 27px; }
  .amp { font-size: 84px; }
  .brand-name { font-family: "Poppins", sans-serif; font-weight: 800; fill: var(--white); }
  .brand-dot { fill: var(--pink-soft); }
  .hours { font-family: "Poppins", sans-serif; font-style: italic; font-weight: 700; font-size: 12px; }
</style>
</head>
<body>
<svg class="storefront" viewBox="0 0 1500 1500" xmlns="http://www.w3.org/2000/svg" role="img" aria-label="Bakery storefront window film: Enjoy Life. Eat Cake.">
  <defs>
    <g id="pane-film">
      <rect class="pane-black" x="0" y="398" width="295" height="566"/>
      <g role="img" aria-label="Pink frosting band along the top of the pane">
        <rect class="band-hot" x="0" y="398" width="295" height="62"/>
        <rect class="band-soft" x="0" y="460" width="295" height="7"/>
      </g>
      <g role="img" aria-label="Pink frosting band along the bottom of the pane">
        <rect class="band-soft" x="0" y="892" width="295" height="8"/>
        <rect class="band-hot" x="0" y="900" width="295" height="64"/>
      </g>
      <rect class="band-hot" x="0" y="976" width="295" height="124"/>
    </g>
  </defs>

  <!-- Frame and mullions -->
  <rect class="frame" x="24" y="398" width="1452" height="702"/>

  <!-- Window panes -->
  <use href="#pane-film" class="window-pane" transform="translate(24,0)"/>
  <use href="#pane-film" class="window-pane" transform="translate(332,0)"/>
  <use href="#pane-film" class="window-pane" transform="translate(873,0)"/>
  <use href="#pane-film" class="window-pane" transform="translate(1181,0)"/>

  <!-- Door transom and door -->
  <g class="door">
    <rect class="pane-black" x="640" y="398" width="220" height="185"/>
    <rect class="pane-black" x="669" y="625" width="162" height="430"/>
  </g>

  <!-- Transom bars -->
  <rect class="frame" x="24" y="583" width="616" height="13"/>
  <rect class="frame" x="860" y="583" width="616" height="13"/>
  <rect class="frame" x="640" y="583" width="220" height="13"/>
  <rect class="frame" x="24" y="964" width="604" height="12"/>
  <rect class="frame" x="873" y="964" width="603" height="12"/>

  <!-- Headlines -->
  <text class="copy copy-white headline" x="60" y="558">Enjoy</text>
  <text class="copy copy-white headline" x="482" y="558" text-anchor="middle">Life.</text>
  <text class="copy copy-white headline" x="1014" y="552" text-anchor="middle">Eat</text>
  <text class="copy copy-white headline" x="1340" y="552" text-anchor="middle">Cake.</text>

  <!-- Pane 1 copy -->
  <text class="copy copy-pink line-md" x="58" y="674">Custom</text>
  <text class="copy copy-white line-lg" x="58" y="722">Cakes</text>
  <text class="copy copy-white line-lg" x="58" y="800">Holiday</text>
  <text class="copy copy-pink line-md" x="58" y="848">Desserts</text>

  <!-- Pane 2 copy -->
  <text class="copy copy-pink line-lg" x="480" y="674" text-anchor="middle">Order</text>
  <text class="copy copy-white line-lg" x="480" y="722" text-anchor="middle">Online</text>
  <text class="copy copy-pink line-sm" x="480" y="785" text-anchor="middle">bellamies</text>
  <text class="copy copy-white line-sm" x="575" y="811" text-anchor="end">.com</text>

  <!-- Pane 4 copy -->
  <text class="copy copy-white line-md" x="1024" y="673" text-anchor="middle">Next day</text>
  <text class="copy copy-pink line-lg" x="1024" y="722" text-anchor="middle">Pick-up</text>
  <text class="copy copy-pink line-lg" x="1028" y="800" text-anchor="middle">Delivery</text>
  <text class="copy copy-white line-md" x="1026" y="848" text-anchor="middle">Available</text>

  <!-- Pane 5 copy -->
  <text class="copy copy-white line-md" x="1330" y="672" text-anchor="middle">Cupcakes</text>
  <text class="copy copy-pink line-lg" x="1330" y="722" text-anchor="middle">Cookies</text>
  <text class="copy copy-white amp" x="1330" y="804" text-anchor="middle">&amp;</text>
  <text class="copy copy-white line-lg" x="1330" y="854" text-anchor="middle">Sweets</text>

  <!-- Brand name, transom -->
  <g class="brand">
    <circle class="brand-dot" cx="750" cy="462" r="18"/>
    <text class="brand-name" x="750" y="506" font-size="21" text-anchor="middle" letter-spacing="1">BELLAMIE'S</text>
    <text class="brand-name" x="750" y="527" font-size="13" text-anchor="middle" letter-spacing="2">BAKE SHOPPE</text>
  </g>

  <!-- Brand name and hours, door -->
  <g class="brand">
    <circle class="brand-dot" cx="750" cy="724" r="12"/>
    <text class="brand-name" x="750" y="756" font-size="15" text-anchor="middle" letter-spacing="1">BELLAMIE'S</text>
    <text class="brand-name" x="750" y="770" font-size="9" text-anchor="middle" letter-spacing="1.5">BAKE SHOPPE</text>
  </g>
  <g class="hours" text-anchor="middle">
    <text class="copy-pink" x="750" y="796">Hours:</text>
    <text class="copy-white" x="750" y="810">Monday - Saturday</text>
    <text class="copy-pink" x="750" y="824">8.00 am - 10.00 pm</text>
    <text class="copy-white" x="750" y="850">Sunday</text>
    <text class="copy-pink" x="750" y="864">11.00 am - 5.00 pm</text>
  </g>
</svg>
</body>
</html>
```